marketing card

I need a fun and striking Marketing card to introduce our new office to attract new patients
our website is smilepathwaykids@mailbrook.net for more ideas
add coupon for $25.00 off your next filling
add coupon for free teeth whitening
make the card 9x6 size ,
The card downloaded I like rediscover your smile
free teeth whitening after exam,x-rays & cleaning
Target Market(s)
population in our area , anyone looking for a dental office
Industry/Entity Type
Health Care
Font styles to use
Serif
Colors
33a6d7
9bcb3c
Requirements
Must have
- Coupon for $25 off if you need a filling
- free whitening after teeth cleaning, x-rays & exam
- Our hygienist will come to you if you are home bound or in a nursing home facility
Nice to have
- want to be inviting and non intimating, we see all ages

```html
<!DOCTYPE html>
<html lang="en">
<head>
<meta charset="utf-8">
<title>Smile Pathway – Marketing Card</title>
<link href="https://fonts.googleapis.com/css2?family=Oswald:wght@500;600&family=Roboto:wght@400;500&display=swap" rel="stylesheet">
<style>
  :root {
    --page-bg: #e9edf1;
    --card-bg: #a9d5f6;
    --card-bg-light: #c4e2fa;
    --band-blue: #1a93d2;
    --navy-box: #142f45;
    --brand-navy: #2a3f96;
    --text-dark-blue: #183e8c;
    --white: #ffffff;
  }
  * { box-sizing: border-box; margin: 0; padding: 0; }
  html, body { width: 1200px; height: 1200px; overflow: hidden; }
  body {
    background: var(--page-bg);
    font-family: "Roboto", Arial, sans-serif;
    position: relative;
  }
  .card {
    position: absolute;
    left: 195px;
    width: 810px;
    height: 540px;
    overflow: hidden;
    background: linear-gradient(135deg, var(--card-bg-light), var(--card-bg) 60%);
    box-shadow: 0 6px 18px rgba(0,0,0,.18);
  }
  .card--front { top: 40px; }
  .card--back { top: 620px; }
  .card__shapes { position: absolute; inset: 0; }
  .photo { position: absolute; inset: 0; }
  .photo--front {
    background: linear-gradient(120deg, #dfe7ef, #f2f4f6 45%, #e6d7b8 75%, #f4f4f4);
    clip-path: polygon(306px 0, 810px 0, 810px 391px, 96px 391px);
  }
  .photo--back {
    background: linear-gradient(110deg, #6d7a80, #c9c3ba 40%, #efece6 70%, #f7f7f7);
    clip-path: polygon(275px 0, 810px 0, 810px 331px, 96px 331px);
  }
  .brand {
    position: absolute;
    left: 26px; top: 22px;
    display: flex; align-items: center; gap: 8px;
    font-family: "Oswald", sans-serif;
    font-weight: 600;
    font-size: 34px;
    color: var(--brand-navy);
    line-height: 1;
  }
  .brand__dot {
    width: 14px; height: 14px; border-radius: 50%;
    background: var(--brand-navy);
  }
  .offer-box {
    position: absolute;
    left: 33px;
    width: 361px;
    background: var(--navy-box);
    color: var(--white);
    text-align: center;
    padding: 3px 4px;
    line-height: 1.2;
  }
  .offer-box__title { font-size: 16px; }
  .offer-box__detail { font-size: 9.5px; }
  .offer-box__text { font-size: 12.5px; }
  .badge {
    position: absolute;
    width: 140px; height: 140px;
    display: flex; flex-direction: column; align-items: center; justify-content: center;
    transform: rotate(-60deg);
    color: var(--white);
    text-align: center;
    line-height: 1.05;
  }
  .badge__amount { font-family: "Roboto", sans-serif; font-weight: 500; font-size: 21px; }
  .badge__note { font-size: 12px; font-style: normal; }
  .band-text {
    position: absolute;
    left: 90px; right: 10px;
    text-align: center;
    color: var(--white);
  }
  .band-text__headline {
    font-family: "Oswald", sans-serif;
    font-weight: 600;
    letter-spacing: .5px;
    line-height: 1.1;
  }
  .card--front .band-text { top: 392px; }
  .card--front .band-text__headline { font-size: 48px; }
  .card--front .band-text__sub { font-size: 18.5px; font-weight: 500; margin-top: 2px; }
  .card--back .band-text { top: 333px; }
  .card--back .band-text__headline { font-size: 33px; }
  .card--back .band-text__sub { font-size: 20px; font-weight: 500; }
  .card--back .band-text__note { font-size: 16px; font-weight: 500; margin-top: 2px; }
  .contact__title {
    position: absolute; top: 453px; left: 0; right: 0;
    padding-left: 110px;
    text-align: center;
    font-family: "Oswald", sans-serif; font-weight: 500;
    font-size: 24px; color: var(--text-dark-blue);
  }
  .contact__item {
    position: absolute;
    display: flex; gap: 6px;
    font-size: 14.5px; line-height: 1.35;
    color: var(--text-dark-blue);
  }
  .contact__item svg { flex: none; margin-top: 3px; }
  .contact__item--address { left: 78px; top: 494px; }
  .contact__item--phone { left: 500px; top: 494px; }
  .contact__item--email { left: 500px; top: 514px; }
</style>
</head>
<body>

<section class="card card--front">
  <div class="photo photo--front" role="img" aria-label="Photo of a dentist in safety glasses and mask working with a dental instrument"></div>
  <svg class="card__shapes" width="810" height="540" viewBox="0 0 810 540">
    <line x1="306" y1="0" x2="96" y2="391" stroke="var(--band-blue)" stroke-width="6"/>
    <polygon points="96,391 810,391 810,504 35,504" fill="var(--band-blue)"/>
    <circle cx="79" cy="343" r="63" fill="var(--band-blue)"/>
  </svg>
  <div class="brand"><span class="brand__dot"></span>Smile Pathway</div>
  <div class="offer-box" style="top:126px;">
    <div class="offer-box__title">$99</div>
    <div class="offer-box__detail">EXAM , X-RAYS &amp; CLEANING NEW PATIENTS ONLY EXPIRES IN 4 WEEKS</div>
  </div>
  <div class="offer-box" style="top:174px;">
    <div class="offer-box__title">FREE</div>
    <div class="offer-box__detail">TEETH WHIENING AFTER EXAM , X-RAYS &amp; CLEANING</div>
  </div>
  <div class="badge" style="left:14px; top:282px;">
    <span class="badge__amount">$25 % OFF</span>
    <span class="badge__note">if you need a filling</span>
  </div>
  <div class="band-text">
    <h1 class="band-text__headline">REDISCOVER YOUR SMILE!</h1>
    <p class="band-text__sub">You will stand Taller, Laugh Longer &amp; Smile more. A smile can change your life !</p>
  </div>
</section>

<section class="card card--back">
  <div class="photo photo--back" role="img" aria-label="Photo of a gloved clinician handling sample tubes in a bright lab"></div>
  <svg class="card__shapes" width="810" height="540" viewBox="0 0 810 540">
    <line x1="275" y1="0" x2="96" y2="331" stroke="var(--band-blue)" stroke-width="6"/>
    <polygon points="96,331 810,331 810,443 35,443" fill="var(--band-blue)"/>
    <circle cx="79" cy="284" r="63" fill="var(--band-blue)"/>
  </svg>
  <div class="brand"><span class="brand__dot"></span>Smile Pathway</div>
  <div class="offer-box" style="top:109px; padding:4px;">
    <div class="offer-box__text">Want to be inviting and non intimating,<br>We see all ages</div>
  </div>
  <div class="offer-box" style="top:159px;">
    <div class="offer-box__title">CALL TODAY !</div>
    <div class="offer-box__detail">555-201-7384</div>
  </div>
  <div class="badge" style="left:14px; top:223px;">
    <span class="badge__amount">$25 % OFF</span>
    <span class="badge__note">if you need a filling</span>
  </div>
  <div class="band-text">
    <h2 class="band-text__headline">YOUR DENTAL BENEFITS HAVE RENEWED</h2>
    <p class="band-text__sub">Free whitening after teeth cleaning, x-rays &amp; exam</p>
    <p class="band-text__note">Our hygienist will come to you if you are home bound or in a nursing home facility</p>
  </div>
  <h3 class="contact__title">- CONTACT INFO -</h3>
  <div class="contact__item contact__item--address">
    <svg width="10" height="13" viewBox="0 0 10 13"><path d="M5 0a5 5 0 0 0-5 5c0 3.5 5 8 5 8s5-4.5 5-8a5 5 0 0 0-5-5zm0 7a2 2 0 1 1 0-4 2 2 0 0 1 0 4z" fill="var(--text-dark-blue)"/></svg>
    <span>2270 W. Maple Ridge Rd. #140 Brookdale, UT 84999<br>(Northwest corner of Harbor Grill)</span>
  </div>
  <div class="contact__item contact__item--phone">
    <svg width="12" height="12" viewBox="0 0 24 24"><path d="M6.6 10.8a15 15 0 0 0 6.6 6.6l2.2-2.2a1 1 0 0 1 1-.25 11.4 11.4 0 0 0 3.6.57 1 1 0 0 1 1 1V20a1 1 0 0 1-1 1A17 17 0 0 1 3 4a1 1 0 0 1 1-1h3.5a1 1 0 0 1 1 1c0 1.25.2 2.45.57 3.57a1 1 0 0 1-.25 1z" fill="var(--text-dark-blue)"/></svg>
    <span>555-201-7384</span>
  </div>
  <div class="contact__item contact__item--email">
    <svg width="12" height="9" viewBox="0 0 12 9"><rect width="12" height="9" fill="var(--text-dark-blue)"/><path d="M0 0l6 5 6-5" stroke="#c4e2fa" fill="none"/></svg>
    <span>smilepathwaykids@mailbrook.net</span>
  </div>
</section>

</body>
</html>
```